Wedding Company needs Brochure Design

FOR THIS PROJECT, WE ARE LOOKING FOR A BROCHURE. WHOEVER WE CHOOSE AS THE WINNING BROCHURE DESIGN WILL THEN DESIGN OUR WEBSITE AND BUSINESS CARD.

We're are looking to expand our brochure by making it a circle and adding 6 inside pages of information with a front and back cover. The pages will be as follows:

Front
About us
About us pictures
Wedding Planning
Wedding planning pictures
Lighting & Decor
Lighting & decor pictures
Back

We've uploaded a picture of our current brochure... so you can get an idea of what we've liked before. Please give us your creative input & design ideas. We've put together a "mock" brochure for you to take a look at as well. As you can see we need your help to properly lay out pictures so that the pages look full and the pictures pop and catches our clients attention.

A few words to describe our brochure would be "elegance", "class", "tasteful" and "colorful". We want to be able to portray that we are luxurious and innovative for the higher end brides and at the same time catering to the budget friendly brides.

Currently, we are waiting on a few pictures from the photographers and we are hoping to have them in a few days... In the meantime we've placed pictures we took from our phone as place holders.

Industry/Entity Type

Catering

```html
<!DOCTYPE html>
<html lang="en">
<head>
<meta charset="utf-8">
<title>Glowline Events – Circle Brochure</title>
<link rel="stylesheet" href="https://fonts.googleapis.com/css2?family=Cormorant+Garamond:ital,wght@1,500;1,600&family=Italianno&display=swap">
<style>
  :root {
    --paper: #fbf2c4;
    --paper-light: #fdf8e0;
    --paper-deep: #f6e6a4;
    --gold: #d9b25a;
    --gold-dark: #b8872c;
    --purple: #6b2d8c;
    --purple-soft: #8a52a8;
    --page-bg: #ffffff;
  }
  * { box-sizing: border-box; }
  html, body {
    margin: 0;
    width: 1200px;
    height: 2775px;
    overflow: hidden;
    background: var(--page-bg);
  }
  .canvas { position: relative; width: 1200px; height: 2775px; }
  .spread { position: absolute; left: 0; width: 1200px; height: 580px; }
  .panel {
    position: absolute;
    top: 0;
    width: 580px;
    height: 580px;
    border-radius: 50%;
    overflow: hidden;
    background: radial-gradient(circle at 50% 45%, var(--paper-light) 0%, var(--paper) 55%, var(--paper-deep) 100%);
    box-shadow: 0 0 0 2px var(--gold);
  }
  .panel--left { left: 30px; }
  .panel--right { left: 590px; }
  .ring {
    position: absolute; inset: 0; width: 100%; height: 100%;
    pointer-events: none;
  }
  .ring circle { fill: none; stroke: var(--gold); stroke-width: 1.5; }
  .arc-text {
    font-family: "Cormorant Garamond", serif;
    font-style: italic; font-weight: 600;
    font-size: 24px; fill: var(--gold-dark); letter-spacing: 1px;
  }
  .photo { position: absolute; }
  .brand {
    position: absolute; left: 0; right: 0;
    display: flex; align-items: center; justify-content: center; gap: 10px;
  }
  .brand__dot { width: 18px; height: 18px; border-radius: 50%; background: var(--gold); }
  .brand__name {
    font-family: "Cormorant Garamond", serif;
    font-style: italic; font-weight: 600;
    font-size: 30px; letter-spacing: 2px; text-transform: uppercase;
    color: var(--purple);
  }
  .address {
    position: absolute; left: 0; right: 0; top: 372px; margin: 0; text-align: center;
    font-family: "Cormorant Garamond", serif; font-style: italic; font-weight: 600;
    font-size: 15px; color: var(--gold-dark);
  }
  .social {
    position: absolute; left: 165px; top: 408px; width: 260px;
    display: grid; grid-template-columns: 1fr 1fr; row-gap: 14px; column-gap: 14px;
    font-family: "Cormorant Garamond", serif; font-style: italic; font-weight: 600;
    font-size: 13px; color: var(--purple); white-space: nowrap;
  }
  .social__item { display: flex; align-items: center; gap: 7px; }
  .social__mark { width: 18px; height: 18px; border-radius: 3px; background: var(--purple-soft); flex: none; }
  .tagline {
    position: absolute; left: 0; right: 0; top: 348px; margin: 0; text-align: center;
    font-family: "Cormorant Garamond", serif; font-style: italic; font-weight: 600;
    font-size: 25px; color: var(--purple);
  }
  .body-copy {
    position: absolute;
    font-family: "Cormorant Garamond", serif; font-style: italic; font-weight: 500;
    color: var(--purple); text-align: center;
  }
  .body-copy p { margin: 0 0 7px; }
  .about-copy { left: 115px; width: 350px; top: 262px; font-size: 12.5px; line-height: 17px; }
  .section-title {
    position: absolute; left: 0; right: 0; text-align: center;
    font-family: "Italianno", cursive; color: var(--purple); margin: 0; font-weight: 400;
    white-space: nowrap;
  }
  .rule {
    position: absolute; left: 160px; width: 260px; height: 2px;
    background: linear-gradient(90deg, transparent, var(--gold) 20%, var(--gold) 80%, transparent);
  }
  .service-box {
    position: absolute;
    background: var(--paper-light);
    border: 2px solid var(--gold);
    box-shadow: inset 0 0 0 5px var(--paper-light), inset 0 0 0 6px var(--gold);
    padding: 16px 18px;
    display: flex; align-items: center; justify-content: center;
  }
  .service-list {
    list-style: none; margin: 0; padding: 0;
    display: grid; grid-template-columns: auto auto; column-gap: 16px;
    font-family: "Cormorant Garamond", serif; font-style: italic; font-weight: 600;
    color: var(--purple); white-space: nowrap;
  }
  .service-list li { display: flex; align-items: center; gap: 8px; }
  .service-list li::before {
    content: ""; width: 10px; height: 10px; border-radius: 50%;
    background: var(--purple-soft); flex: none;
  }
  .service-list--lighting { grid-auto-flow: column; grid-template-rows: repeat(7, 23px); font-size: 14px; }
  .service-list--planning { grid-auto-flow: row; grid-auto-rows: 25px; font-size: 14px; }
  .service-list--planning .span-both { grid-column: 1 / span 2; }
  .badge {
    position: absolute; left: 268px; top: 500px; width: 44px; height: 40px;
    background: #ffffff; border: 2px solid #9fb3c8; border-radius: 3px;
  }
</style>
</head>
<body>
<main class="canvas">

  <!-- Covers -->
  <section class="spread spread--covers" style="top:40px">
    <div class="panel panel--left">
      <div class="brand" style="top:300px">
        <span class="brand__dot"></span><span class="brand__name">Glowline Events</span>
      </div>
      <p class="address">1420 Harbor Lane Suite B Seaview, CA 90210</p>
      <div class="social">
        <span class="social__item"><span class="social__mark"></span>/glowlineevents</span>
        <span class="social__item"><span class="social__mark"></span>@glowlineevents</span>
        <span class="social__item"><span class="social__mark"></span>@glowlineevents</span>
        <span class="social__item"><span class="social__mark"></span>/glowlineevents</span>
      </div>
      <svg class="ring" viewBox="0 0 580 580">
        <circle cx="290" cy="290" r="276"/>
        <path id="back-left-arc" d="M 28 290 A 262 262 0 0 0 290 552" fill="none"/>
        <path id="back-right-arc" d="M 290 552 A 262 262 0 0 0 552 290" fill="none"/>
        <text class="arc-text"><textPath href="#back-left-arc" startOffset="50%" text-anchor="middle">www.glowlineevents.com</textPath></text>
        <text class="arc-text"><textPath href="#back-right-arc" startOffset="55%" text-anchor="middle">555.014.2290</textPath></text>
      </svg>
    </div>
    <div class="panel panel--right">
      <div class="brand" style="top:92px">
        <span class="brand__dot"></span><span class="brand__name">Glowline Events</span>
      </div>
      <div class="photo" role="img" aria-label="Guests gathered on a lit dance floor at a celebration"
           style="left:95px;top:152px;width:390px;height:180px;border-radius:50%;background:radial-gradient(ellipse at 50% 45%, #5c4a7a 0%, #2e2440 60%, rgba(46,36,64,0) 100%)"></div>
      <p class="tagline">weddings. anniversaries. special events.</p>
      <svg class="ring" viewBox="0 0 580 580">
        <circle cx="290" cy="290" r="276"/>
        <path id="front-left-arc" d="M 28 290 A 262 262 0 0 0 290 552" fill="none"/>
        <path id="front-right-arc" d="M 290 552 A 262 262 0 0 0 552 290" fill="none"/>
        <text class="arc-text"><textPath href="#front-left-arc" startOffset="50%" text-anchor="middle">www.glowlineevents.com</textPath></text>
        <text class="arc-text"><textPath href="#front-right-arc" startOffset="55%" text-anchor="middle">555.014.2290</textPath></text>
      </svg>
    </div>
  </section>

  <!-- About us -->
  <section class="spread spread--about" style="top:730px">
    <div class="panel panel--left">
      <div class="photo" role="img" aria-label="Reception hall washed in magenta and purple lighting"
           style="left:140px;top:85px;width:300px;height:160px;border:3px solid #fff;background:linear-gradient(180deg,#c05ab8 0%,#7a2f86 45%,#241a2c 100%)"></div>
      <div class="body-copy about-copy">
        <p>Based in coastal California, Glowline Events is a wedding and event lighting and decor company. We treat every celebration as a canvas, shaping mood with colour and glow. Whether you dream of a grand ballroom or a garden party, we tailor each detail to your vision.</p>
        <p>Glowline Events is a sister company of a respected entertainment group with years of shows behind it. With that backing, we bring stage-level lighting and design to every wedding, delivered by a crew that is personal and polished.</p>
        <p>Let us help you take your event from ordinary to extraordinary!</p>
      </div>
      <div class="badge"></div>
      <svg class="ring" viewBox="0 0 580 580"><circle cx="290" cy="290" r="276"/></svg>
    </div>
    <div class="panel panel--right">
      <div class="photo" role="img" aria-label="White floral centerpieces on a dark table"
           style="left:105px;top:120px;width:180px;height:220px;background:linear-gradient(180deg,#e9e6df 0%,#9c958a 55%,#2c2622 100%)"></div>
      <div class="photo" role="img" aria-label="Outdoor lounge under strings of warm lights"
           style="left:295px;top:130px;width:180px;height:125px;background:linear-gradient(180deg,#2a2018 0%,#8a6a2a 60%,#d9b35a 100%)"></div>
      <div class="photo" role="img" aria-label="Evening reception lit in blue and pink"
           style="left:105px;top:350px;width:180px;height:120px;background:linear-gradient(180deg,#1a1e3a 0%,#3b3f8a 55%,#b0508e 100%)"></div>
      <div class="photo" role="img" aria-label="Tiered white wedding cake with lavender ribbon"
           style="left:295px;top:265px;width:180px;height:195px;background:linear-gradient(180deg,#6a3e8c 0%,#c9b2d8 50%,#8a5aa8 100%)"></div>
      <svg class="ring" viewBox="0 0 580 580"><circle cx="290" cy="290" r="276"/></svg>
    </div>
  </section>

  <!-- Lighting and decor -->
  <section class="spread spread--lighting" style="top:1420px">
    <div class="panel panel--left">
      <h2 class="section-title" style="top:62px;font-size:50px">Lighting and Decor</h2>
      <div class="rule" style="top:126px"></div>
      <div class="body-copy" style="left:95px;width:390px;top:140px;font-size:15px;line-height:21px">
        <p>Let our experts draw attention to your carefully chosen centerpieces, surround your guests with your event colors and even write your initials in light. Looking for something romantic? Imagine dining under lanterns and chandeliers. Ready to transform your event to a hot dance club? Let our experts swirl and strobe light over your guests and dancefloor. We offer a wide range of lighting services including, but not limited to:</p>
      </div>
      <div class="service-box" style="left:140px;top:318px;width:300px;height:190px">
        <ul class="service-list service-list--lighting">
          <li>Pinspots</li><li>Intelligent Lighting</li><li>Uplighting</li><li>Special FX</li>
          <li>Dance Floors</li><li>Draping</li><li>Café Lights</li>
          <li>Staging</li><li>Search Lights</li><li>Vinyl</li><li>Video Projection</li>
          <li>Monograms</li><li>Chiavari Chairs</li><li>Custom Designs</li>
        </ul>
      </div>
      <svg class="ring" viewBox="0 0 580 580"><circle cx="290" cy="290" r="276"/></svg>
    </div>
    <div class="panel panel--right">
      <div class="photo" role="img" aria-label="Performer on a stage with red and amber lighting"
           style="left:80px;top:170px;width:240px;height:120px;background:linear-gradient(180deg,#4a1a18 0%,#a3402e 55%,#2a1410 100%)"></div>
      <div class="photo" role="img" aria-label="Ceiling draped in fabric glowing purple"
           style="left:330px;top:170px;width:170px;height:120px;background:linear-gradient(180deg,#d7b8ea 0%,#9a5ec4 55%,#4e2870 100%)"></div>
      <div class="photo" role="img" aria-label="Tented reception lit in violet and blue"
           style="left:80px;top:300px;width:240px;height:120px;background:linear-gradient(180deg,#2a2f6a 0%,#7a4ab0 55%,#b46ab8 100%)"></div>
      <div class="photo" role="img" aria-label="Projected monogram on a dance floor"
           style="left:330px;top:300px;width:170px;height:120px;background:radial-gradient(ellipse at 50% 50%,#ffffff 0%,#d8d4e4 45%,#6a6280 100%)"></div>
      <svg class="ring" viewBox="0 0 580 580"><circle cx="290" cy="290" r="276"/></svg>
    </div>
  </section>

  <!-- Wedding planning -->
  <section class="spread spread--planning" style="top:2110px">
    <div class="panel panel--left">
      <h2 class="section-title" style="top:100px;font-size:36px">Wedding Planning and Coordination</h2>
      <div class="rule" style="top:148px"></div>
      <div class="body-copy" style="left:95px;width:390px;top:160px;font-size:13px;line-height:18px">
        <p>With all the success and joy we have experienced in providing our expertise and quality service, we are now prepared to include the planning and execution of your entire wedding. We've partnered together with top notch vendors in the Southern California area to put together a phenomenal wedding full of unforgettable memories for both the happy couple and their guests. We are your one stop shop for all things wedding!</p>
      </div>
      <div class="body-copy" style="left:0;right:0;top:304px;font-size:15px">We can assist you in the following:</div>
      <div class="service-box" style="left:125px;top:333px;width:330px;height:160px">
        <ul class="service-list service-list--planning">
          <li>Decor Items</li><li>Cake</li>
          <li>Florist</li><li>Photographer</li>
          <li>Caterer</li><li>Rental Linens</li>
          <li>DJ &amp; Band Services</li><li>Bartending Services</li>
          <li class="span-both">Planning and Coordination</li>
        </ul>
      </div>
      <svg class="ring" viewBox="0 0 580 580"><circle cx="290" cy="290" r="276"/></svg>
    </div>
    <div class="panel panel--right">
      <div class="photo" role="img" aria-label="Ceremony space with soft white draping"
           style="left:100px;top:110px;width:230px;height:120px;background:linear-gradient(180deg,#f3e6e4 0%,#d9bfc0 55%,#a88a8c 100%)"></div>
      <div class="photo" role="img" aria-label="Outdoor scene at dusk"
           style="left:340px;top:110px;width:140px;height:120px;background:linear-gradient(180deg,#6e7a94 0%,#48506a 55%,#2a2c36 100%)"></div>
      <div class="photo" role="img" aria-label="Purple and pink floral arrangement"
           style="left:100px;top:240px;width:100px;height:110px;background:linear-gradient(180deg,#b37ac4 0%,#7a3e8a 55%,#4a6a3a 100%)"></div>
      <div class="photo" role="img" aria-label="Reception room with a dance floor in blue light"
           style="left:210px;top:240px;width:270px;height:110px;background:linear-gradient(180deg,#1c2a46 0%,#3e5a8a 55%,#141a26 100%)"></div>
      <div class="photo" role="img" aria-label="Garden ceremony aisle"
           style="left:100px;top:360px;width:230px;height:110px;background:linear-gradient(180deg,#9ab27a 0%,#5e7a48 55%,#3a4a2c 100%)"></div>
      <div class="photo" role="img" aria-label="Evening reception with pink and blue uplighting"
           style="left:340px;top:360px;width:140px;height:110px;background:linear-gradient(180deg,#c96aa8 0%,#6a3e8a 55%,#283a6a 100%)"></div>
      <svg class="ring" viewBox="0 0 580 580"><circle cx="290" cy="290" r="276"/></svg>
    </div>
  </section>

</main>
</body>
</html>
```